Concierge Healthcare Business Card Design and Logo

We need a logo and business card design for a new company called "Sound Keeper". We will provide concierge audiological care, hearing aids, hearing exams, custom hearing protection etc to patients in the comfort of their homes and offices. We would like a sleek and modern design preferably with an Ear related logo.

Target Market(s)

People with hearing loss, Hunters, Musicians
My usual clientele are older individuals so usually 50+ years old

Industry/Entity Type

Health Care

Contact Information for Business Card

Clara Whitfield, AuD
Audiologist
512-418-2967
soundkeeper@mailvista.net
www.soundkeeperclinic.net

Logo Text

Sound Keeper

Number of Pages Required

3 page

```html
<!DOCTYPE html>
<html lang="en">
<head>
<meta charset="utf-8">
<title>Sound Keeper – Business Card</title>
<link href="https://fonts.googleapis.com/css2?family=Questrial&family=Montserrat:wght@400;600&display=swap" rel="stylesheet">
<style>
  :root {
    --brand-blue: #1a76c6;
    --ink: #111111;
    --paper: #ffffff;
    --stage: #e9ebee;
    --rule-grey: #9aa0a6;
  }
  * { margin: 0; padding: 0; box-sizing: border-box; }
  html, body { width: 1200px; height: 900px; overflow: hidden; }
  body {
    background: var(--stage);
    position: relative;
    font-family: "Questrial", "Century Gothic", sans-serif;
  }
  .card {
    position: absolute;
    left: 270px;
    width: 660px;
    height: 377px;
    border-radius: 22px;
    overflow: hidden;
    box-shadow: 0 10px 28px rgba(0,0,0,0.18);
  }
  /* Back side */
  .card-back {
    top: 50px;
    background: var(--brand-blue);
    color: var(--paper);
    text-align: center;
  }
  .back-mark {
    position: absolute;
    left: 50%;
    top: 62px;
    width: 120px;
    height: 120px;
    margin-left: -60px;
    border: 2px solid var(--paper);
    border-radius: 50%;
  }
  .back-name {
    position: absolute;
    left: 0; right: 0;
    top: 200px;
    font-size: 54px;
    letter-spacing: 1px;
  }
  .back-web {
    position: absolute;
    left: 0; right: 0;
    top: 292px;
    font-family: "Montserrat", sans-serif;
    font-size: 17px;
    letter-spacing: 0.5px;
  }
  /* Front side */
  .card-front {
    top: 470px;
    background: var(--paper);
  }
  .front-band { position: absolute; inset: 0; }
  .front-title {
    position: absolute;
    left: 34px;
    top: 36px;
    font-size: 82px;
    color: var(--ink);
    letter-spacing: 1px;
    line-height: 1;
  }
  .title-rule {
    position: absolute;
    left: 300px;
    top: 140px;
    width: 320px;
    height: 2px;
    background: var(--brand-blue);
  }
  .person {
    position: absolute;
    left: 44px;
    top: 166px;
    font-family: "Montserrat", sans-serif;
  }
  .person-name {
    color: var(--brand-blue);
    font-weight: 600;
    font-size: 24px;
  }
  .person-role {
    color: var(--ink);
    font-size: 16px;
    margin-top: 2px;
  }
  .person-bar {
    position: absolute;
    left: 0;
    top: 190px;
    width: 40px;
    height: 26px;
    background: var(--ink);
    border-right: 8px solid var(--brand-blue);
  }
  .contacts {
    position: absolute;
    left: 44px;
    top: 272px;
    list-style: none;
    font-family: "Montserrat", sans-serif;
    font-size: 17px;
    color: var(--paper);
    line-height: 28px;
  }
  .contacts li { display: flex; align-items: center; gap: 10px; }
  .contacts svg { width: 14px; height: 14px; fill: none; stroke: var(--paper); stroke-width: 2; }
  .front-mark {
    position: absolute;
    right: 14px;
    top: 150px;
    width: 104px;
    height: 104px;
    border-radius: 50%;
    background: var(--paper);
    border: 2px solid var(--rule-grey);
    display: flex;
    align-items: center;
    justify-content: center;
    text-align: center;
    font-size: 17px;
    line-height: 1.1;
    color: var(--ink);
  }
</style>
</head>
<body>

  <section class="card card-back">
    <div class="back-mark"></div>
    <div class="back-name">Sound Keeper</div>
    <div class="back-web">www.soundkeeperclinic.net</div>
  </section>

  <section class="card card-front">
    <svg class="front-band" viewBox="0 0 660 377" preserveAspectRatio="none">
      <polygon points="0,262 250,262 560,168 660,168 660,377 0,377" fill="var(--brand-blue)"/>
    </svg>
    <h1 class="front-title">Sound Keeper</h1>
    <div class="title-rule"></div>
    <div class="person-bar"></div>
    <div class="person">
      <div class="person-name">Clara Whitfield, AuD</div>
      <div class="person-role">Audiologist</div>
    </div>
    <ul class="contacts">
      <li>
        <svg viewBox="0 0 16 16"><path d="M4 1.5l2.5 3-1.5 1.5c1 2 2.5 3.5 4.5 4.5l1.5-1.5 3 2.5-1.5 2.5C7.5 14 2 8.5 1.5 3z"/></svg>
        512-418-2967
      </li>
      <li>
        <svg viewBox="0 0 16 16"><rect x="1.5" y="3.5" width="13" height="9"/><path d="M1.5 3.5l6.5 5 6.5-5"/></svg>
        soundkeeper@mailvista.net
      </li>
      <li>
        <svg viewBox="0 0 16 16"><circle cx="8" cy="8" r="6.5"/><path d="M1.5 8h13M8 1.5c-3 3.5-3 9.5 0 13M8 1.5c3 3.5 3 9.5 0 13"/></svg>
        www.soundkeeperclinic.net
      </li>
    </ul>
    <div class="front-mark">Sound<br>Keeper</div>
  </section>

</body>
</html>
```